Brindle Works PPT design

We are looking for a fresh and funky PPT design that is both eye-catching and allows room/whitespace for us to get the content across. We are a social media agency based in China and our logo although simple sort of reflects the nature of the company. There are two main tasks for this PPT, one as a business card to show-case our case-studies, but also as a back-drop to our pitch presentations and other client presentations. These presentations are a mix of visuals, text and graphs. The key message we want to get across is that we are professional, creative and fresh. We think that using our four support colours may work but are open to suggestions.
Current website www.brindleworks-demo.com
Reason: Hi All,
as we have just guaranteed the payment we extended the deadline to allow for more submissions. Please bear with us.
Thanks,
Brindle Works Team
Reason: To see more designs, we extend the deadline to March 18, 2014. Thanks.
Target Market(s)
Marketing CMO's, company CEO's, product managers, social media managers
Industry/Entity Type
Business
Look and feel

```html
<!DOCTYPE html>
<html lang="en">
<head>
<meta charset="utf-8">
<title>Brindle Works – Presentation Template</title>
<link href="https://fonts.googleapis.com/css2?family=Open+Sans:wght@300;400;600;700&family=Ubuntu:wght@400;500&display=swap" rel="stylesheet">
<style>
:root{
  --bg:#a9b1b6;
  --purple:#6a1b8e;
  --purple-deep:#5a1580;
  --magenta:#e0007a;
  --green:#8fce4e;
  --orange:#e35f35;
  --ink:#2f2e3b;
  --ink-2:#393846;
  --text:#4a4a5a;
  --muted:#7c7c8a;
  --white:#ffffff;
  --row-alt:#f2f2f4;
}
*{box-sizing:border-box;margin:0;padding:0}
html,body{width:1064px;height:1200px;overflow:hidden;background:var(--bg)}
body{font-family:"Open Sans",Arial,sans-serif;color:var(--text)}
.canvas{width:1200px;height:1354px;position:relative;transform:scale(.88667);transform-origin:0 0;background:var(--bg)}
.slide{position:absolute;width:582px;height:437px;overflow:hidden;background:var(--white)}
.s1{left:14px;top:10px}.s2{left:605px;top:10px}
.s3{left:14px;top:458px}.s4{left:605px;top:458px}
.s5{left:14px;top:907px}.s6{left:605px;top:907px}

/* content slide header & footer */
.slide-head{height:55px;border-bottom:1px solid #e3e3e8;text-align:center;background:#fbfbfc}
.slide-title{font-weight:300;font-size:29px;color:var(--purple);letter-spacing:.5px;padding-top:4px;line-height:34px}
.slide-sub{font-size:10.5px;color:var(--muted);letter-spacing:.3px}
.slide-sub b{color:var(--ink);font-weight:700}
.slide-foot{position:absolute;left:0;bottom:0;width:100%;height:36px;background:var(--ink);display:flex;align-items:center;padding-left:10px}
.foot-brand{color:var(--white);font-weight:700;font-size:14px;margin-right:14px;letter-spacing:-.2px}
.foot-label{font-size:10.5px;color:#e8e8ee;letter-spacing:.2px}
.foot-label b{font-weight:700}
.foot-label .to{color:#9b2a6a}
.foot-label .client{color:var(--magenta);font-weight:700}
.foot-label .client span{font-weight:400}
.page-no{position:absolute;right:14px;bottom:6px;font-size:9px;color:var(--magenta)}

/* tables */
.table-block{position:absolute;top:72px;width:260px}
.table-block.light{left:22px}.table-block.dark{left:301px}
.table-title{font-size:16px;color:var(--ink);display:flex;align-items:center;gap:6px;height:22px}
.table-title b{font-weight:700}
.table-title span{font-weight:400}
.plan{width:260px;border-collapse:collapse;margin-top:9px;font-size:7px;table-layout:fixed}
.plan th{height:25px;font-size:9px;font-weight:400;text-align:center}
.plan td{height:25.3px;text-align:center;line-height:1.3;padding:0 3px}
.plan .c-item{width:36px}.plan .c-step{width:97px}.plan .c-resp{width:65px}
.plan td.num{font-size:10px}
.plan tfoot td{height:25px;font-size:10px}
.light .plan th{background:var(--ink);color:var(--magenta)}
.light .plan td{color:#555}
.light .plan tbody tr:nth-child(odd){background:var(--white)}
.light .plan tbody tr:nth-child(even){background:var(--row-alt)}
.light .plan td.num{color:var(--magenta)}
.light .plan tfoot td{background:var(--magenta);color:var(--white)}
.dark .plan th{background:var(--ink);color:var(--white);font-weight:600}
.dark .plan td{background:var(--ink-2);color:#7a7987;border-bottom:1px solid #34333f}
.dark .plan td.num{background:var(--purple);color:var(--white);border-bottom-color:#5f1882}
.dark .plan tfoot td{background:var(--ink);color:var(--white)}

/* chapter slides */
.chapter{color:var(--white)}
.chapter.purple{background:var(--purple)}
.chapter.green{background:var(--green)}
.chapter .texture{position:absolute;inset:0}
.chapter.purple .texture{background:radial-gradient(circle at 60% 45%,rgba(255,255,255,.07),rgba(0,0,0,0) 60%)}
.chapter.green .texture{background:radial-gradient(circle at 60% 45%,rgba(255,255,255,.12),rgba(0,0,0,0) 60%)}
.chapter-icon{position:absolute;left:120px;top:169px}
.chapter-rule{position:absolute;left:237px;top:180px;width:1px;height:87px;background:rgba(255,255,255,.7)}
.chapter-heading{position:absolute;left:259px;top:176px;font-family:"Ubuntu",sans-serif;font-weight:500;font-size:21px;letter-spacing:.3px}
.chapter-subtitle{position:absolute;left:259px;top:201px;font-family:"Ubuntu",sans-serif;font-size:17px}
.purple .chapter-subtitle{color:var(--green)}
.green .chapter-subtitle{color:var(--purple-deep)}
.corner-brand{position:absolute;right:14px;bottom:14px;font-size:13px;font-weight:700;color:var(--white)}

/* bullets */
.bullets{position:absolute;left:24px;top:122px;width:510px;list-style:none}
.bullets li{position:relative;padding-left:18px;font-size:9.5px;line-height:13px;color:#5a5a6a;margin-bottom:12.7px}
.bullets li::before{content:"";position:absolute;left:0;top:4px;border-left:4px solid var(--purple);border-top:3px solid transparent;border-bottom:3px solid transparent}
.bullets b{font-weight:700;color:var(--ink)}
.list-icon{position:absolute;right:8px;top:366px}

/* graphs */
.graph-title{position:absolute;top:78px;font-size:16.5px;color:var(--ink)}
.graph-title b{font-weight:700}
.graph-title.main{left:28px}.graph-title.second{left:331px}
.graph-svg{position:absolute;left:0;top:0}
.graph-notes{position:absolute;top:310px;width:220px;list-style:none}
.graph-notes.main{left:40px}.graph-notes.second{left:324px}
.graph-notes li{position:relative;padding-left:14px;font-size:7.6px;line-height:11px;color:#5a5a6a;margin-bottom:12px}
.graph-notes li::before{content:"";position:absolute;left:0;top:3px;border-left:3px solid var(--magenta);border-top:2.5px solid transparent;border-bottom:2.5px solid transparent}
.graph-notes b{font-weight:700;color:var(--ink)}

/* closing */
.closing{background:var(--ink);color:var(--white)}
.closing .texture{position:absolute;inset:0;background:radial-gradient(circle at 55% 40%,rgba(255,255,255,.04),rgba(0,0,0,0) 60%)}
.closing-brand{position:absolute;left:0;right:0;top:158px;text-align:center;font-size:64px;font-weight:700;letter-spacing:-1px;color:var(--white)}
.closing-mark{position:absolute;left:212px;top:254px;width:14px;height:12px;background:var(--magenta)}
.contact{position:absolute;left:16px;top:345px;font-size:8px;line-height:11px}
.contact h4{font-size:10px;font-weight:700;margin-bottom:1px}
.contact .gap{height:14px}
.site{position:absolute;right:14px;bottom:17px;font-size:9.5px}
.stripe{position:absolute;left:0;bottom:0;width:100%;height:3px;display:flex}
.stripe i{flex:1}
</style>
</head>
<body>
<div class="canvas">

  <!-- Slide: Color style tables -->
  <section class="slide s1">
    <header class="slide-head">
      <h1 class="slide-title">COLOR STYLE TABLES</h1>
      <p class="slide-sub">CHOOSE FROM A <b>LIGHT</b> OR <b>DARK</b> THEME</p>
    </header>

    <div class="table-block light">
      <h2 class="table-title">
        <svg width="18" height="14" viewBox="0 0 18 14"><rect x="1" y="1" width="16" height="12" fill="none" stroke="#6a1b8e" stroke-width="1.6"/><path d="M1 5h16M1 9h16M6 1v12M12 1v12" stroke="#6a1b8e" stroke-width="1.2"/></svg>
        <span><b>Light</b> Theme</span>
      </h2>
      <table class="plan">
        <colgroup><col class="c-item"><col class="c-step"><col class="c-resp"><col></colgroup>
        <thead><tr><th>Item</th><th>Step/Action</th><th>Responsible</th><th>Target Date</th></tr></thead>
        <tbody>
          <tr><td class="num">1</td><td>Business X, Y, Z high level needs</td><td>Business X, Y, Z</td><td>5/24/2013</td></tr>
          <tr><td class="num">2</td><td>Understand current situation and safety mana</td><td>Business X, Y, Z</td><td>5/31/2013</td></tr>
          <tr><td class="num">3</td><td>Submit Proposal</td><td>Business X, Y, Z</td><td>6/3/2013</td></tr>
          <tr><td class="num">4</td><td>Review Proposal</td><td>Business X, Y, Z</td><td>TBD</td></tr>
          <tr><td class="num">5</td><td>Prepare Final Proposal &amp; Statement of Work (SOW)</td><td>Business X, Y, Z</td><td>TBD</td></tr>
          <tr><td class="num">6</td><td>Complete and sign SOW</td><td>Business X, Y, Z</td><td>TBD</td></tr>
          <tr><td class="num">7</td><td>Schedule project start date</td><td>Business X, Y, Z</td><td>TBD</td></tr>
          <tr><td class="num">8</td><td>Kick-off Project</td><td>Business X, Y, Z</td><td>TBD</td></tr>
          <tr><td class="num">9</td><td>Complete Project</td><td>Business X, Y, Z</td><td>TBD</td></tr>
        </tbody>
        <tfoot><tr><td colspan="4">* Additional Information</td></tr></tfoot>
      </table>
    </div>

    <div class="table-block dark">
      <h2 class="table-title">
        <svg width="18" height="14" viewBox="0 0 18 14"><rect x="1" y="1" width="16" height="12" fill="none" stroke="#6a1b8e" stroke-width="1.6"/><path d="M1 5h16M1 9h16M6 1v12M12 1v12" stroke="#6a1b8e" stroke-width="1.2"/></svg>
        <span><b>Dark</b> Theme</span>
      </h2>
      <table class="plan">
        <colgroup><col class="c-item"><col class="c-step"><col class="c-resp"><col></colgroup>
        <thead><tr><th>Item</th><th>Step/Action</th><th>Responsible</th><th>Target Date</th></tr></thead>
        <tbody>
          <tr><td class="num">1</td><td>Business X, Y, Z high level needs</td><td>Business X, Y, Z</td><td>5/24/2013</td></tr>
          <tr><td class="num">2</td><td>Understand current situation and safety mana</td><td>Business X, Y, Z</td><td>5/31/2013</td></tr>
          <tr><td class="num">3</td><td>Submit Proposal</td><td>Business X, Y, Z</td><td>6/3/2013</td></tr>
          <tr><td class="num">4</td><td>Review Proposal</td><td>Business X, Y, Z</td><td>TBD</td></tr>
          <tr><td class="num">5</td><td>Prepare Final Proposal &amp; Statement of Work (SOW)</td><td>Business X, Y, Z</td><td>TBD</td></tr>
          <tr><td class="num">6</td><td>Complete and sign SOW</td><td>Business X, Y, Z</td><td>TBD</td></tr>
          <tr><td class="num">7</td><td>Schedule project start date</td><td>Business X, Y, Z</td><td>TBD</td></tr>
          <tr><td class="num">8</td><td>Kick-off Project</td><td>Business X, Y, Z</td><td>TBD</td></tr>
          <tr><td class="num">9</td><td>Complete Project</td><td>Business X, Y, Z</td><td>TBD</td></tr>
        </tbody>
        <tfoot><tr><td colspan="4">* Additional Information</td></tr></tfoot>
      </table>
    </div>

    <footer class="slide-foot">
      <span class="foot-brand">Brindle Works</span>
      <span class="foot-label"><b>COMPANY</b> PRESENTATION <span class="to">to</span> <span class="client">Business<span>/client</span></span></span>
      <span class="page-no">7</span>
    </footer>
  </section>

  <!-- Slide: Chapter (purple) -->
  <section class="slide s2 chapter purple">
    <div class="texture" role="img" aria-label="Faint network pattern of connected dots and social icons"></div>
    <svg class="chapter-icon" width="100" height="100" viewBox="0 0 100 100">
      <circle cx="50" cy="50" r="48" fill="none" stroke="#fff" stroke-width="2.2"/>
      <rect x="38" y="33" width="36" height="38" fill="#fff"/>
      <g fill="#6a1b8e"><rect x="44" y="48" width="5" height="5"/><rect x="51" y="48" width="5" height="5"/><rect x="58" y="48" width="5" height="5"/><rect x="65" y="48" width="5" height="5"/><rect x="44" y="56" width="5" height="5"/><rect x="51" y="56" width="5" height="5"/><rect x="58" y="56" width="5" height="5"/><rect x="65" y="56" width="5" height="5"/><rect x="44" y="64" width="5" height="4"/><rect x="51" y="64" width="5" height="4"/></g>
      <circle cx="37" cy="41" r="15" fill="#6a1b8e" stroke="#fff" stroke-width="2.5"/>
      <path d="M37 32v10h7" fill="none" stroke="#fff" stroke-width="2.2"/>
    </svg>
    <div class="chapter-rule"></div>
    <h2 class="chapter-heading">NEW CHAPTER HEADING</h2>
    <p class="chapter-subtitle">New Chapter Subtitle</p>
    <span class="corner-brand">Brindle Works</span>
  </section>

  <!-- Slide: Text with bullets -->
  <section class="slide s3">
    <header class="slide-head">
      <h1 class="slide-title">JUST TEXT WITH BULLETS</h1>
      <p class="slide-sub">YOU CAN CUSTOMIZE YOUR BULLETS</p>
    </header>
    <ul class="bullets">
      <li><b>Aenean</b> ridiculus tortor quis interdum id habitant ad, natoque consectetuer nisl auctor libero quisque euismod ante inceptos malesuada ligula mattis.</li>
      <li><b>Aenean</b> ridiculus tortor quis interdum id habitant ad, natoque consectetuer nisl auctor libero quisque euismod ante inceptos malesuada ligula mattis.</li>
      <li>Nulla, netus pulvinar pellentesque porttitor purus maecenas tellus hac nulla lacus. Lorem. Nostra laoreet nulla, dis cursus nascetur dolor odio Eu Magna molestie montes dui mus cursus habitasse mauris tempor.</li>
      <li>Varius inceptos <b>nascetur</b> mollis dui aptent ultrices. Pretium pulvinar ante lobortis convallis lectus netus vitae penatibus eros at blandit. Parturient.</li>
      <li>Varius inceptos <b>nascetur</b> mollis dui aptent ultrices. Pretium pulvinar ante lobortis convallis lectus netus vitae penatibus eros at blandit. Parturient.</li>
    </ul>
    <svg class="list-icon" width="34" height="28" viewBox="0 0 34 28" fill="#6a1b8e">
      <circle cx="4" cy="4" r="3.5"/><circle cx="4" cy="14" r="3.5"/><circle cx="4" cy="24" r="3.5"/>
      <rect x="10" y="2" width="24" height="4"/><rect x="10" y="12" width="24" height="4"/><rect x="10" y="22" width="24" height="4"/>
    </svg>
    <footer class="slide-foot">
      <span class="foot-brand">Brindle Works</span>
      <span class="foot-label"><b>COMPANY</b> PRESENTATION <span class="to">to</span> <span class="client">Business<span>/client</span></span></span>
      <span class="page-no">9</span>
    </footer>
  </section>

  <!-- Slide: Chapter (green) -->
  <section class="slide s4 chapter green">
    <div class="texture" role="img" aria-label="Faint network pattern of connected dots and social icons"></div>
    <svg class="chapter-icon" width="100" height="100" viewBox="0 0 100 100">
      <circle cx="50" cy="50" r="48" fill="none" stroke="#fff" stroke-width="2.2"/>
      <g fill="#fff">
        <circle cx="50" cy="30" r="13"/><circle cx="31" cy="61" r="13"/><circle cx="68" cy="61" r="13"/>
      </g>
      <g fill="#8fce4e">
        <circle cx="50" cy="27" r="4"/><path d="M42 38a8 7 0 0 1 16 0z"/>
        <circle cx="31" cy="58" r="4"/><path d="M23 69a8 7 0 0 1 16 0z"/>
        <circle cx="68" cy="58" r="4"/><path d="M60 69a8 7 0 0 1 16 0z"/>
      </g>
    </svg>
    <div class="chapter-rule"></div>
    <h2 class="chapter-heading">NEW CHAPTER HEADING</h2>
    <p class="chapter-subtitle">New Chapter Subtitle</p>
    <span class="corner-brand">Brindle Works</span>
  </section>

  <!-- Slide: Color style graphs -->
  <section class="slide s5">
    <header class="slide-head">
      <h1 class="slide-title">COLOR STYLE GRAPHS</h1>
      <p class="slide-sub">CHOOSE TO USE BETWEEN <b>MAIN</b> AND <b>SECONDARY</b> COLOR THEMES</p>
    </header>
    <h2 class="graph-title main"><b>Graph</b> Main Colors</h2>
    <h2 class="graph-title second"><b>Graph</b> Secondary Colors</h2>

    <svg class="graph-svg" width="582" height="400" viewBox="0 0 582 400" font-family="Open Sans, sans-serif">
      <!-- area chart -->
      <g font-size="8" fill="#555" text-anchor="end">
        <text x="41" y="124">100</text><text x="41" y="166">75</text><text x="41" y="207">50</text><text x="41" y="249">25</text><text x="41" y="291">0</text>
      </g>
      <g font-size="8" fill="#555" text-anchor="middle">
        <text x="48" y="301">2007</text><text x="120" y="301">2008</text><text x="192" y="301">2009</text><text x="264" y="301">2010</text>
      </g>
      <polygon points="48,238 120,254 192,265 264,288 48,288" fill="#e0007a"/>
      <polygon points="48,196 120,216 192,171 264,184 264,288 48,288" fill="#6a1b8e"/>
      <polygon points="48,258 120,243 192,196 264,128 264,288 48,288" fill="#8fce4e"/>
      <line x1="48" y1="288" x2="264" y2="288" stroke="#444" stroke-width="1"/>

      <!-- pie chart -->
      <path d="M419 203 L374.4 286.9 A95 95 0 0 1 457.6 116.2 Z" fill="#e0007a"/>
      <path d="M419 203 L509.8 230.8 A95 95 0 0 1 374.4 286.9 Z" fill="#6a1b8e"/>
      <path d="M419 203 L497.8 149.9 A95 95 0 0 1 509.8 230.8 Z" fill="#e35f35"/>
      <path d="M427 192 L465.6 105.2 A95 95 0 0 1 505.8 138.9 Z" fill="#8fce4e"/>
      <g font-size="10.5" fill="#fff" text-anchor="middle">
        <text x="378" y="182">50%</text><text x="475" y="154">9%</text><text x="483" y="203">14%</text><text x="439" y="267">28%</text>
      </g>
      <g font-size="8" fill="#333">
        <circle cx="501" cy="269" r="4" fill="#8fce4e"/><text x="509" y="272">2007</text>
        <circle cx="538" cy="269" r="4" fill="#e35f35"/><text x="546" y="272">2008</text>
        <circle cx="501" cy="280" r="4" fill="#6a1b8e"/><text x="509" y="283">2009</text>
        <circle cx="538" cy="280" r="4" fill="#e0007a"/><text x="546" y="283">2010</text>
      </g>
    </svg>

    <ul class="graph-notes main">
      <li><b>Aenean</b> ridiculus tortor quis interdum id habitant ad, natoque consectetuer nisl auctor libero quisque euismod ante inceptos malesuada ligula mattis.</li>
      <li>Varius inceptos <b>nascetur</b> mollis dui aptent ultrices. Pretium pulvinar ante lobortis convallis lectus netus vitae penatibus eros at blandit. Parturient.</li>
    </ul>
    <ul class="graph-notes second">
      <li><b>Aenean</b> ridiculus tortor quis interdum id habitant ad, natoque consectetuer nisl auctor libero quisque euismod ante inceptos malesuada ligula mattis.</li>
      <li>Varius inceptos <b>nascetur</b> mollis dui aptent ultrices. Pretium pulvinar ante lobortis convallis lectus netus vitae penatibus eros at blandit. Parturient.</li>
    </ul>

    <footer class="slide-foot">
      <span class="foot-brand">Brindle Works</span>
      <span class="foot-label"><b>COMPANY</b> PRESENTATION <span class="to">to</span> <span class="client">Business<span>/client</span></span></span>
      <span class="page-no">11</span>
    </footer>
  </section>

  <!-- Slide: Closing -->
  <section class="slide s6 closing">
    <div class="texture" role="img" aria-label="Faint network pattern of connected dots and social icons"></div>
    <p class="closing-brand">Brindle Works</p>
    <span class="closing-mark"></span>
    <div class="contact">
      <h4>Contact us:</h4>
      <p>888-888-8888</p>
      <p>info@brindleworks-demo.com</p>
      <div class="gap"></div>
      <h4>Central Office:</h4>
      <p>Address Line 1</p>
      <p>Address Line 2</p>
    </div>
    <p class="site">www.brindleworks-demo.com</p>
    <div class="stripe"><i style="background:var(--green)"></i><i style="background:var(--purple)"></i><i style="background:var(--magenta)"></i><i style="background:var(--orange)"></i></div>
  </section>

</div>
</body>
</html>
```